Fontenot Bayou Grillhouse (Owners Card)

Need a classy, but modern business card. I have included a promotional card for the steakhouse. I need one for myself (the owner) that is more professional.

Target Market(s)

General Public

Industry/Entity Type

Food service

Contact Information for Business Card

Name, business address, phone number, email, logo

Font styles to use
Serif
Sans Serif
Decorative
Script

Requirements
Must have
• My name (Darvel Pruitt), business address (327 Oakmere Street), phone number (510) 493-2615, email (Dpruittkr4@mailvane.example. On the back of the card: Psalms 27 1 The LORD is my light and my salvation— whom shall I fear? The LORD is the stronghold of my life— of whom shall I be afraid? 2 When the wicked advance against me to devour me, it is my enemies and my foes who will stumble and fall. 3 Though an army besiege me, my heart will not fear; though war break out against me, even then I will be confident.
Nice to have
• Something that’s bold, but modern and professional.

```html
<!DOCTYPE html>
<html lang="en">
<head>
<meta charset="utf-8">
<title>Fontenot Bayou Grillhouse – Owner Card</title>
<link rel="stylesheet" href="https://fonts.googleapis.com/css2?family=Cinzel:wght@500;700&family=Arimo:wght@400&display=swap">
<style>
  :root {
    --backdrop: #3b3b3b;
    --card: #2b2b2b;
    --edge-green: #2bd62b;
    --name-green: #1fc21f;
    --text-light: #e9e9e9;
    --text-muted: #bdbdbd;
    --icon-orange: #ff6a00;
    --accent-red: #e0281c;
    --grad-green: #22d61e;
    --grad-yellow: #e2c400;
    --grad-orange: #ff7a00;
    --grad-red: #ee1b14;
  }
  * { box-sizing: border-box; margin: 0; padding: 0; }
  html, body { width: 1200px; height: 803px; overflow: hidden; }
  body {
    background: var(--backdrop);
    font-family: "Arimo", Arial, sans-serif;
    position: relative;
  }
  .card {
    position: absolute;
    top: 250px;
    width: 540px;
    height: 308px;
    background: var(--card);
    border-radius: 22px;
    border-bottom: 3px solid var(--edge-green);
    border-right: 2px solid var(--edge-green);
    box-shadow: 0 18px 40px rgba(0,0,0,.45);
    overflow: hidden;
  }
  .card-front { left: 45px; }
  .card-back { left: 615px; }

  /* front */
  .brand {
    position: absolute;
    left: 34px; top: 0; bottom: 0;
    width: 240px;
    display: flex;
    align-items: center;
    gap: 12px;
  }
  .brand-dot {
    flex: none;
    width: 16px; height: 16px;
    border-radius: 50%;
    background: var(--name-green);
  }
  .brand-name {
    font-family: "Cinzel", Georgia, serif;
    font-weight: 700;
    font-size: 26px;
    line-height: 1.15;
    color: var(--name-green);
  }
  .divider {
    position: absolute;
    left: 290px; top: 60px;
    width: 1px; height: 190px;
    background: linear-gradient(#555, #8a8a8a, #555);
  }
  .owner {
    position: absolute;
    left: 312px; top: 66px;
    right: 20px;
  }
  .owner-name {
    font-family: "Cinzel", Georgia, serif;
    font-weight: 500;
    font-size: 23px;
    letter-spacing: 0.5px;
    white-space: nowrap;
    color: var(--name-green);
  }
  .owner-title { font-size: 13px; color: var(--text-muted); margin-top: 2px; }
  .address { margin-top: 18px; font-size: 13.5px; line-height: 1.35; color: var(--text-light); }
  .contact-list { list-style: none; margin-top: 14px; font-size: 13.5px; line-height: 1.55; color: var(--text-light); }
  .contact-list li { display: flex; align-items: center; gap: 8px; white-space: nowrap; }
  .contact-list svg { width: 12px; height: 12px; flex: none; }

  /* back */
  .verses {
    position: absolute;
    left: 28px; top: 26px;
    width: 250px;
    font-size: 11.5px;
    line-height: 1.38;
    color: var(--text-light);
  }
  .verse + .verse { margin-top: 8px; }
  .verse-rule {
    display: block;
    width: 30px; height: 2px;
    margin-bottom: 6px;
    background: linear-gradient(90deg, var(--accent-red), var(--grad-green));
  }
  .mask-art {
    position: absolute;
    right: 0; top: 24px;
    width: 250px; height: 260px;
    border-radius: 120px 0 0 120px;
    background: linear-gradient(90deg, var(--grad-green), var(--grad-yellow) 45%, var(--grad-orange) 72%, var(--grad-red));
  }
</style>
</head>
<body>
  <section class="card card-front">
    <div class="brand">
      <span class="brand-dot"></span>
      <span class="brand-name">Fontenot Bayou Grillhouse</span>
    </div>
    <span class="divider"></span>
    <div class="owner">
      <h1 class="owner-name">DARVEL PRUITT</h1>
      <p class="owner-title">Owner</p>
      <p class="address">327 Oakmere Street<br>Larkdale, CA 94718</p>
      <ul class="contact-list">
        <li>
          <svg viewBox="0 0 12 12"><path d="M2.5 1l2 2.2-1 1.3a6 6 0 0 0 4 4l1.3-1L11 9.5 9.6 11C5 11 1 7 1 2.4z" fill="var(--icon-orange)"/></svg>
          (510) 493-2615
        </li>
        <li>
          <svg viewBox="0 0 12 12"><rect x="1" y="2.5" width="10" height="7" rx="1" fill="var(--icon-orange)"/><path d="M1.5 3l4.5 3.5L10.5 3" stroke="var(--card)" stroke-width="1" fill="none"/></svg>
          Dpruittkr4@mailvane.example
        </li>
        <li>
          <svg viewBox="0 0 12 12"><circle cx="6" cy="6" r="5" fill="var(--icon-orange)"/><path d="M1 6h10M6 1c-2 2.5-2 7.5 0 10M6 1c2 2.5 2 7.5 0 10" stroke="var(--card)" stroke-width=".8" fill="none"/></svg>
          www.fontenotbayou.example
        </li>
      </ul>
    </div>
  </section>

  <section class="card card-back">
    <div class="verses">
      <p class="verse">The LORD is my light and my salvation— whom shall I fear? The LORD is the stronghold of my life— of whom shall I be afraid?</p>
      <p class="verse"><span class="verse-rule"></span>When the wicked advance against me to devour me, it is my enemies and my foes who will stumble and fall.</p>
      <p class="verse"><span class="verse-rule"></span>Though an army besiege me, my heart will not fear; though war break out against me, even then I will be confident.</p>
    </div>
    <div class="mask-art" role="img" aria-label="Large carnival mask illustration with feathered plume in a green-to-yellow-to-red gradient foil"></div>
  </section>
</body>
</html>
```